Business Card Design Project

We are VT Meridian, a recruitment company based in London. We require a new business card design in order to present our business. We work in a number of areas recruiting professional in areas such as engineering and rail. Most of our work is based in the Middle East so our cards must have a universal, professional feel.

Visit our website: http://www.vt-meridian.example.co.uk/ for more info

Industry/Entity Type

Business

Requirements
Must have
• Must be double sided

Must feature the companies logo on both sides of the card

Should incorporate the primary colours of the logo

Must be professional and contemporary, to fit in with the logo

Info: Name: Colin Prewett certRP MREC
Senior Recruitment Consultant
Address: 7 Quarry Row Fulwell London N41QZ
T: +44 (0)203 555 0147
M: +44 (0)7700 900 318
E: cprewett@vt-meridian.example.co.uk
W www.vt-meridian.example.co.uk
Nice to have
• A modern style card

```html
<!DOCTYPE html>
<html lang="en">
<head>
<meta charset="utf-8">
<title>VT Meridian – Business Card</title>
<link rel="stylesheet" href="https://fonts.googleapis.com/css2?family=Quicksand:wght@400;500&family=Arimo:wght@400&display=swap">
<style>
  :root {
    --stage: #c8c6c6;
    --teal: #009a82;
    --teal-light: #05a48c;
    --grey-band: #8f8b8b;
    --brand-grey: #8a8787;
    --text-grey: #6f6c6c;
    --paper: #ffffff;
  }
  * { box-sizing: border-box; margin: 0; padding: 0; }
  html, body { width: 1200px; height: 446px; overflow: hidden; }
  body {
    position: relative;
    background: var(--stage);
    font-family: "Arimo", Arial, sans-serif;
  }
  .card { position: absolute; width: 517px; height: 297px; overflow: hidden; }

  /* Front */
  .card-front {
    left: 68px; top: 83px;
    background: radial-gradient(circle at 45% 50%, var(--teal-light) 0%, var(--teal) 70%);
  }
  .front-lockup {
    position: absolute; left: 0; right: 0; top: 128px;
    text-align: center; color: var(--paper);
  }
  .front-name {
    font-family: "Quicksand", sans-serif; font-weight: 500;
    font-size: 50px; line-height: 1; letter-spacing: -0.5px;
  }
  .front-tagline {
    margin-top: 4px;
    font-family: "Quicksand", sans-serif; font-weight: 500;
    font-size: 8px; letter-spacing: 4.4px;
  }

  /* Back */
  .card-back {
    left: 600px; top: 83px;
    background: linear-gradient(120deg, var(--paper) 55%, #f1f1f1 100%);
    box-shadow: 0 3px 8px rgba(0,0,0,0.25);
  }
  .band-top { position: absolute; left: 50px; top: 0; width: 39px; height: 36px; background: var(--teal); }
  .band-bottom { position: absolute; left: 50px; top: 98px; width: 39px; height: 199px; background: var(--grey-band); }
  .brand-mark {
    position: absolute; left: 38px; top: 37px; width: 62px; height: 62px;
    border-radius: 50%; background: var(--teal);
  }
  .brand-name {
    position: absolute; left: 114px; top: 38px;
    font-family: "Quicksand", sans-serif; font-weight: 500;
    font-size: 50px; line-height: 1; color: var(--brand-grey); letter-spacing: -0.5px;
  }
  .brand-tagline {
    position: absolute; left: 116px; top: 92px;
    font-family: "Quicksand", sans-serif; font-weight: 500;
    font-size: 7.5px; letter-spacing: 3.6px; color: var(--brand-grey);
  }
  .person { position: absolute; left: 119px; top: 127px; }
  .person-name { font-size: 17px; color: var(--teal); line-height: 1.1; }
  .person-title { font-size: 9px; color: var(--text-grey); }
  .address {
    position: absolute; left: 120px; top: 194px;
    font-size: 10.5px; line-height: 14px; color: var(--text-grey); font-style: normal;
  }
  .contacts { position: absolute; left: 297px; top: 194px; list-style: none; }
  .contacts li {
    display: flex; align-items: center; gap: 4px;
    font-size: 10px; line-height: 11.7px; color: var(--text-grey);
  }
  .contacts svg { width: 9px; height: 9px; fill: var(--teal); flex: none; }
</style>
</head>
<body>

<section class="card card-front" aria-label="Business card front">
  <div class="front-lockup">
    <div class="front-name">VT Meridian</div>
    <div class="front-tagline">PROFESSIONAL &amp; TECHNICAL RECRUITMENT</div>
  </div>
</section>

<section class="card card-back" aria-label="Business card back">
  <div class="band-top"></div>
  <div class="band-bottom"></div>
  <div class="brand-mark"></div>
  <div class="brand-name">VT Meridian</div>
  <div class="brand-tagline">PROFESSIONAL &amp; TECHNICAL RECRUITMENT</div>

  <div class="person">
    <div class="person-name">Colin Prewett certRP MREC</div>
    <div class="person-title">Senior Recruitment Consultant</div>
  </div>

  <address class="address">7 Quarry Row<br>Fulwell London N41QZ</address>

  <ul class="contacts">
    <li><svg viewBox="0 0 10 10"><path d="M1 4c0-2 2-3 4-3s4 1 4 3H7V3H3v1zM2 5h6l1 4H1z"/></svg>+44 (0)203 555 0147</li>
    <li><svg viewBox="0 0 10 10"><rect x="2.5" y="0" width="5" height="10" rx="1"/><rect x="3.5" y="1.5" width="3" height="4" fill="#fff"/></svg>+44 (0)7700 900 318</li>
    <li><svg viewBox="0 0 10 10"><rect x="0" y="2" width="10" height="6"/><path d="M0 2l5 3 5-3" stroke="#fff" stroke-width="0.8" fill="none"/></svg>cprewett@vt-meridian.example.co.uk</li>
    <li><svg viewBox="0 0 10 10"><circle cx="5" cy="5" r="4.5"/><path d="M0.5 5h9M5 0.5v9M5 0.5c-2.5 2.5-2.5 6.5 0 9M5 0.5c2.5 2.5 2.5 6.5 0 9" stroke="#fff" stroke-width="0.6" fill="none"/></svg>www.vt-meridian.example.co.uk</li>
  </ul>
</section>

</body>
</html>
```